Vantor Phone App Design Concept

Design concept, including wireframe and design comps for a basketball themed Vantor Phone app.
Need example of a panorama page with 3 or 4 panels to include game schedule, news and a menu.
Example of a detail page showing game info or player info.
Note this quote is for a design concept.The chosen designer will be asked to work with our development team to build the full app. Familiarity with Balsamiq an advantage
Reason: Designs still in process from interested parties.
Build
Must have
- 1. Must follow Vantor Phone guide lines
2. Must not look like an ulbex app
3. Dark theme and background

```html
<!DOCTYPE html>
<html lang="en">
<head>
<meta charset="utf-8">
<title>Basketball Match – Panorama Concept</title>
<link href="https://fonts.googleapis.com/css2?family=Open+Sans:wght@300;400;700&display=swap" rel="stylesheet">
<style>
  :root {
    --gap: #ffffff;
    --bg-deep: #140b07;
    --bg-warm: #2c1a10;
    --bg-glow: #4a2c18;
    --text: #ffffff;
    --text-soft: #e8e2dc;
    --line: #ffffff;
  }
  html, body {
    margin: 0;
    padding: 0;
    width: 1200px;
    height: 660px;
    overflow: hidden;
    background: var(--gap);
    font-family: "Open Sans", "Segoe UI", sans-serif;
    color: var(--text);
  }
  .canvas {
    position: relative;
    width: 1200px;
    height: 660px;
  }
  .screen {
    position: absolute;
    top: 0;
    height: 660px;
    overflow: hidden;
  }
  .screen--news { left: 0; width: 395px; }
  .screen--menu { left: 405px; width: 393px; }
  .screen--regions { left: 810px; width: 390px; }

  .backdrop {
    position: absolute;
    inset: 0;
    background:
      radial-gradient(circle at 80% 55%, var(--bg-glow) 0%, var(--bg-warm) 35%, transparent 70%),
      linear-gradient(180deg, var(--bg-deep) 0%, var(--bg-warm) 70%, #3a2314 100%);
  }
  .screen--news .backdrop {
    background:
      radial-gradient(circle at 110% 60%, var(--bg-glow) 0%, transparent 55%),
      linear-gradient(180deg, var(--bg-deep) 0%, var(--bg-warm) 100%);
  }
  .screen--regions .backdrop {
    background:
      radial-gradient(circle at 40% 45%, var(--bg-glow) 0%, var(--bg-warm) 40%, transparent 75%),
      linear-gradient(180deg, var(--bg-deep) 0%, var(--bg-warm) 100%);
  }

  .app-title {
    position: absolute;
    top: 24px;
    margin: 0;
    font-weight: 300;
    font-size: 72px;
    line-height: 1;
    white-space: nowrap;
    letter-spacing: -0.5px;
  }
  .screen--news .app-title { left: 26px; }
  .screen--menu .app-title { right: 46px; }

  .section-title {
    position: absolute;
    top: 126px;
    margin: 0;
    font-weight: 300;
    font-size: 39px;
    line-height: 1;
    white-space: nowrap;
  }
  .news-title { left: 24px; }
  .option-title--peek { left: 357px; }
  .option-title { left: 15px; }

  .news-body {
    position: absolute;
    left: 24px;
    top: 180px;
    width: 310px;
    margin: 0;
    font-size: 14.6px;
    font-weight: 400;
    line-height: 36px;
    color: var(--text-soft);
  }

  .menu {
    position: absolute;
    top: 209px;
    margin: 0;
    padding: 0;
    list-style: none;
    font-weight: 300;
    font-size: 24px;
    line-height: 1;
    white-space: nowrap;
  }
  .menu li { height: 80px; }
  .menu--peek { left: 365px; }
  .menu--main { left: 15px; }

  .page-kicker {
    position: absolute;
    left: 25px;
    top: 26px;
    margin: 0;
    font-weight: 300;
    font-size: 24px;
    line-height: 1;
  }
  .page-title {
    position: absolute;
    left: 23px;
    top: 70px;
    margin: 0;
    font-weight: 300;
    font-size: 54px;
    line-height: 1;
  }
  .round-label {
    position: absolute;
    top: 141px;
    margin: 0;
    font-weight: 700;
    font-size: 20px;
    line-height: 1;
    white-space: nowrap;
  }
  .round-label--first { left: 25px; }
  .round-label--second { left: 265px; }

  .team {
    position: absolute;
    left: 25px;
    margin: 0;
    font-weight: 300;
    font-size: 20px;
    line-height: 1;
  }
  .team--a { top: 240px; }
  .team--b { top: 360px; }
  .team--c { top: 474px; }
  .team--d { top: 593px; }

  .bracket {
    position: absolute;
    left: 0;
    top: 0;
  }
</style>
</head>
<body>
<main class="canvas">

  <section class="screen screen--news">
    <div class="backdrop" role="img" aria-label="Dark background photo of a basketball on a textured court"></div>
    <h1 class="app-title">Basketball Match</h1>
    <h2 class="section-title news-title">Latest News</h2>
    <p class="news-body">Lorem ipsum dolor sit amet, consectetuer adipiscing elit, sed diam nonummy nibh euismod tincidunt ut laoreet dolore magna aliquam erat volutpat. Ut wisi enim ad minim veniam, quis nostrud exerci tation ullamcorper suscipit lobortis nisl ut aliquip ex ea commodo consequat.</p>
    <h2 class="section-title option-title--peek">Option</h2>
    <ul class="menu menu--peek">
      <li>Scores</li>
      <li>Brackets</li>
      <li>LastFour</li>
    </ul>
  </section>

  <section class="screen screen--menu">
    <div class="backdrop" role="img" aria-label="Dark background photo of a basketball on a textured court"></div>
    <h1 class="app-title">Basketball Match</h1>
    <h2 class="section-title option-title">Option</h2>
    <ul class="menu menu--main">
      <li>Scores</li>
      <li>Brackets</li>
      <li>LastFour</li>
    </ul>
  </section>

  <section class="screen screen--regions">
    <div class="backdrop" role="img" aria-label="Dark background photo of a basketball on a textured court"></div>
    <p class="page-kicker">Basketball Match</p>
    <h1 class="page-title">REGIONS</h1>
    <h2 class="round-label round-label--first">FIRST ROUND</h2>
    <h2 class="round-label round-label--second">SECOND ROUND</h2>

    <svg class="bracket" width="390" height="660" viewBox="0 0 390 660" aria-hidden="true">
      <g fill="none" stroke="var(--line)" stroke-width="2">
        <polyline points="25,265 232,265 232,388 25,388"/>
        <line x1="232" y1="325" x2="390" y2="325"/>
        <polyline points="25,497 232,497 232,620 25,620"/>
        <line x1="232" y1="548" x2="390" y2="548"/>
      </g>
    </svg>

    <p class="team team--a">TEAM A</p>
    <p class="team team--b">TEAM B</p>
    <p class="team team--c">TEAM C</p>
    <p class="team team--d">TEAM D</p>
  </section>

</main>
</body>
</html>
```